I have a website called Nexa Holdings (nexaholdings.com) that I would like to have redesigned. Most of the content is already created, but I need a new design. You can also see my other website at corbelestates.com. I am open to a new logo or modifying the current logo if you have a good idea. Please feel free to use other images for the home page (and maybe some other locations) if you feel they provide a better look and feel to the website. I prefer a modern look.

Important: You do not have to use the images I've provided for the home page. Feel free to find your own stock photos. You don't have to pay for them unless I select your design.

1) Please use wix.com to make your changes so that I can edit it later.
2) I will need all the graphics files to be saved so I can dowload it for later.
3) I will be adding more content to the site later.
4) This site will likely be transferred over to corbelestates.com so if you make a logo please make one for Nexa Holdings and one for Corbel Estates.
5) You can use other images that you feel would help the look and feel of the website.

Real Estate

Coded - Design and coding required

5+ page

```html
<!DOCTYPE html>
<html lang="en">
<head>
<meta charset="utf-8">
<title>Corbel Estates</title>
<link rel="stylesheet" href="https://fonts.googleapis.com/css2?family=Teko:wght@400;500;600&family=Open+Sans:wght@400;600;700&display=swap">
<style>
:root{
  --blue:#1f9ad8;
  --navy:#0e2d57;
  --sky:#eef4fa;
  --ink:#1d2b3a;
  --muted:#5a6878;
  --white:#ffffff;
}
*{margin:0;padding:0;box-sizing:border-box}
html,body{width:1200px;height:3437px;overflow:hidden;background:#fff}
body{position:relative;font-family:"Open Sans",sans-serif;color:var(--ink)}
.abs{position:absolute}
.head{font-family:"Teko",sans-serif;font-weight:500;text-transform:uppercase;line-height:1}
.btn{position:absolute;display:flex;align-items:center;justify-content:center;border-radius:16px;font-size:10px;font-weight:700;color:#fff;height:28px;white-space:nowrap}
.btn-blue{background:var(--blue)}
.btn-navy{background:var(--navy)}
.photo{position:absolute}

/* hero */
.hero{position:absolute;left:0;top:0;width:1200px;height:621px;background:linear-gradient(180deg,#2a5d92 0%,#2f6ea3 45%,#2d5f86 75%,#1f4b6a 100%);overflow:hidden}
.hero-shade{position:absolute;inset:0}
.brand{position:absolute;display:flex;align-items:center;gap:10px;font-family:"Teko",sans-serif;font-size:22px;letter-spacing:.5px;color:#fff;text-transform:uppercase;white-space:nowrap}
.brand-dot{width:36px;height:36px;border-radius:50%;border:3px solid #fff;flex:none}
.nav-link{position:absolute;top:50px;font-size:11.5px;color:#fff;white-space:nowrap}
.nav-link.active{color:var(--blue)}
.nav-line{position:absolute;left:0;top:111px;width:1200px;height:1px;background:rgba(255,255,255,.25)}
.nav-mark{position:absolute;left:556px;top:109px;width:62px;height:3px;background:var(--blue)}
.call{position:absolute;left:856px;top:45px;font-family:"Teko",sans-serif;font-size:18px;color:#fff;white-space:nowrap}
.hero h1{position:absolute;left:200px;top:254px;font-size:40px;color:#fff;line-height:44px;font-weight:400}
.hero .tag{position:absolute;left:200px;top:401px;font-size:17px;color:#fff}
.dots{position:absolute;left:1080px;top:308px;display:flex;flex-direction:column;gap:5px}
.dots span{width:10px;height:10px;border:1px solid rgba(255,255,255,.8);border-radius:50%}
.dots .on{background:rgba(255,255,255,.8)}

/* about */
.about-bg{position:absolute;left:0;top:621px;width:1200px;height:561px;background:#fff;overflow:hidden}
.frame{position:absolute;left:199px;top:686px;width:389px;height:439px;border:2px solid #9cc8ea;padding:10px}
.frame .photo{position:static;width:100%;height:100%;background:linear-gradient(180deg,#cfe2f2 0%,#7b8591 30%,#5b6470 65%,#6d5847 100%)}
.eyebrow{position:absolute;left:643px;top:755px;font-size:10px;color:var(--blue);display:flex;align-items:center;gap:8px}
.eyebrow:before{content:"";width:62px;height:1px;background:var(--blue)}
.sec-title{position:absolute;font-size:27px;color:var(--navy)}
.sec-title b{color:var(--blue);font-weight:500}
.about-copy{position:absolute;left:643px;width:340px;font-size:9.2px;line-height:18.5px;color:var(--ink)}

/* stats */
.stats{position:absolute;left:0;top:1182px;width:1200px;height:160px;background:var(--blue);overflow:hidden}
.faint{position:absolute;width:80px;height:80px;border-radius:50%;border:6px solid rgba(255,255,255,.25)}
.stat{position:absolute;top:60px;width:200px;text-align:center;color:#fff}
.stat .v{font-family:"Teko",sans-serif;font-size:24px;line-height:1}
.stat .l{font-size:10px;margin-top:2px}

/* projects */
.proj-bg{position:absolute;left:0;top:1342px;width:1200px;height:753px;background:#fff;overflow:hidden}
.proj-img{position:absolute;top:1460px;width:494px;height:429px}
.badge{position:absolute;top:1865px;height:24px;width:190px;background:var(--blue);color:#fff;font-size:9px;font-weight:700;display:flex;align-items:center;padding-left:18px;clip-path:polygon(0 0,90% 0,100% 100%,0 100%)}
.proj-name{position:absolute;top:1909px;font-family:"Teko",sans-serif;font-size:19px;color:var(--navy);white-space:nowrap}
.proj-meta{position:absolute;top:1944px;font-size:8.5px;line-height:14px;color:var(--muted);white-space:nowrap}
.proj-meta span{color:var(--blue)}
.arrow{position:absolute;top:2003px;width:28px;height:28px;border-radius:50%;border:1px solid #b9d7ef;background:#e6f1fa;display:flex;align-items:center;justify-content:center}

/* employment */
.employ{position:absolute;left:0;top:2099px;width:1200px;height:161px;background:var(--blue);overflow:hidden}
.employ h2{position:absolute;left:200px;top:50px;font-size:28px;color:#fff;font-weight:400}
.employ p{position:absolute;left:200px;top:84px;width:500px;font-size:9.5px;line-height:15px;color:#fff}
.employ p span{color:#bfe3f8}

/* team */
.team-bg{position:absolute;left:0;top:2260px;width:1200px;height:556px;overflow:hidden}
.member{position:absolute;top:2376px;width:261px;height:309px;background:linear-gradient(180deg,#4b6a82 0%,#2f4458 55%,#1c2a38 100%)}
.member .who{position:absolute;left:24px;bottom:20px;color:#fff;white-space:nowrap}
.member .n{font-family:"Teko",sans-serif;font-size:15px;line-height:1}
.member .r{font-size:9px}

/* partners */
.col-title{position:absolute;top:2832px;width:300px;text-align:center;font-size:26px;color:var(--navy)}
.col-title b{color:var(--blue);font-weight:500}
.divider{position:absolute;left:600px;top:2811px;width:1px;height:240px;background:#dde6ee}
.mark{position:absolute;transform:translate(-50%,-50%);font-weight:700;font-size:16px;display:flex;align-items:center;gap:6px;white-space:nowrap}
.mark i{width:10px;height:10px;display:inline-block}

/* footer */
.footer{position:absolute;left:0;top:3108px;width:1200px;height:329px;background:linear-gradient(120deg,#123a6c 0%,#0f3360 60%,#0d2b52 100%);overflow:hidden;color:#fff}
.f-head{position:absolute;font-size:10px;font-weight:700;letter-spacing:.3px;white-space:nowrap}
.f-line{position:absolute;left:487px;display:flex;gap:8px;font-size:9px;line-height:13px;align-items:flex-start;white-space:nowrap}
.field{position:absolute;background:#fff;color:var(--muted);font-size:8.5px;padding:5px 8px}
.social{position:absolute;top:3277px;width:24px;height:24px;border-radius:50%;background:var(--blue)}
</style>
</head>
<body>

<!-- hero -->
<section class="hero">
  <div class="photo hero-shade" role="img" aria-label="City skyline at sunset with trees in the foreground, tinted blue"></div>
  <svg class="abs" style="left:0;top:0" width="1200" height="621" aria-hidden="true">
    <polygon points="1200,0 1200,621 720,621" fill="rgba(255,255,255,.06)"/>
    <polygon points="0,621 0,330 300,621" fill="rgba(10,35,70,.25)"/>
  </svg>
  <div class="brand" style="left:94px;top:40px"><span class="brand-dot"></span><span>Corbel Estates</span></div>
  <span class="nav-link active" style="left:571px">Home</span>
  <span class="nav-link" style="left:623px">About Us</span>
  <span class="nav-link" style="left:698px">Strategy</span>
  <span class="nav-link" style="left:761px">Projects</span>
  <div class="call">Call Us (123) 555-0147</div>
  <div class="btn btn-blue" style="left:1009px;top:43px;width:99px">Contact Us</div>
  <div class="nav-line"></div>
  <div class="nav-mark" style="left:559px"></div>
  <h1 class="head">Private Commercial<br>Real Estate Investment and<br>Development Firm</h1>
  <div class="tag">Building Together. Growing Together.</div>
  <div class="btn btn-blue" style="left:200px;top:445px;width:100px">Explore More</div>
  <div class="dots"><span></span><span class="on"></span><span></span><span></span></div>
</section>

<!-- about -->
<section class="about-bg">
  <svg class="abs" style="left:0;top:0" width="1200" height="561" aria-hidden="true">
    <polygon points="1200,0 1200,561 660,561" fill="var(--sky)"/>
    <polygon points="980,0 1200,0 1200,200" fill="#ffffff"/>
  </svg>
</section>
<div class="frame"><div class="photo" role="img" aria-label="Modern multi-storey residential building with brick and glass facade"></div></div>
<div class="eyebrow">Welcome to</div>
<div class="sec-title head" style="left:643px;top:781px"><b>Corbel</b> Estates</div>
<p class="about-copy" style="top:830px">Corbel Estates is a private real estate firm that specializes in the procurement, development, management, and disposition of various commercial real estate asset types including multifamily, industrial, single-family, hospitality, self-storage, and flex. The firm effectuates its strategy by utilizing long-standing relationships to ascertain acquisition and development opportunities within a specific target market.</p>
<p class="about-copy" style="top:960px">Corbel Estates is currently focused on acquisition and development opportunities in the southern portion of the United States ...</p>
<div class="btn btn-navy" style="left:633px;top:1036px;width:75px">About Us</div>

<!-- stats -->
<section class="stats">
  <div class="faint" style="left:61px;top:40px"></div>
  <div class="faint" style="left:1060px;top:40px"></div>
  <div class="stat" style="left:267px"><div class="v">2017</div><div class="l">Year Established</div></div>
  <div class="stat" style="left:422px"><div class="v">DALLAS, TX</div><div class="l">Headquarters</div></div>
  <div class="stat" style="left:577px"><div class="v">$100MM+</div><div class="l">Assets Under Management</div></div>
  <div class="stat" style="left:732px"><div class="v">06</div><div class="l">Current Projects</div></div>
</section>

<!-- projects -->
<section class="proj-bg">
  <svg class="abs" style="left:0;top:0" width="1200" height="753" aria-hidden="true">
    <polygon points="0,0 190,0 0,190" fill="var(--sky)"/>
    <polygon points="1200,380 1200,753 900,753" fill="var(--sky)"/>
  </svg>
</section>
<div class="sec-title head" style="left:0;width:1200px;text-align:center;top:1410px"><b>Our</b> Projects</div>
<div class="photo proj-img" style="left:94px;background:linear-gradient(180deg,#8fc4ea 0%,#cdb89b 40%,#6e8a55 75%,#9a9a98 100%)" role="img" aria-label="Rendering of a four storey residential building with landscaped walkway"></div>
<div class="photo proj-img" style="left:611px;background:linear-gradient(180deg,#7fc1f0 0%,#a8d6f5 35%,#6d5a4f 55%,#5f9a45 78%,#7db055 100%)" role="img" aria-label="Aerial rendering of a multifamily community with courtyard and pool"></div>
<div class="badge" style="left:94px">MULTIFAMILY DEVELOPMENT</div>
<div class="badge" style="left:611px">MULTIFAMILY DEVELOPMENT</div>
<div class="proj-name" style="left:112px">Brookline Harbor Residences</div>
<div class="proj-name" style="left:629px;text-decoration:underline">Lakeview at Cedar Point</div>
<div class="proj-meta" style="left:112px">Class A Multifamily - 176 Units - 4 Story - 159,280 SF - 3 Acres<br><span>Ground-up Development</span></div>
<div class="proj-meta" style="left:629px">Class A Multifamily - 373 Units - 3 Story - 345,297 SF - 24.31 Acres<br><span>Ground-up Development</span></div>
<div class="arrow" style="left:494px"><svg width="10" height="10" viewBox="0 0 10 10"><path d="M6.5 1.5 3 5l3.5 3.5" fill="none" stroke="#1f9ad8" stroke-width="1.5"/></svg></div>
<div class="btn btn-navy" style="left:551px;top:2003px;width:98px">View All</div>
<div class="arrow" style="left:676px"><svg width="10" height="10" viewBox="0 0 10 10"><path d="M3.5 1.5 7 5 3.5 8.5" fill="none" stroke="#1f9ad8" stroke-width="1.5"/></svg></div>

<!-- employment -->
<section class="employ">
  <svg class="abs" style="left:0;top:0" width="1200" height="161" aria-hidden="true">
    <polygon points="0,0 200,0 110,161 0,161" fill="var(--navy)"/>
    <polygon points="1200,0 1200,161 900,161" fill="var(--navy)"/>
  </svg>
  <div class="faint" style="left:61px;top:40px;border-color:rgba(255,255,255,.18)"></div>
  <div class="faint" style="left:1060px;top:40px;border-color:rgba(255,255,255,.18)"></div>
  <h2 class="head">Employment</h2>
  <p>To apply for a job with Corbel Estates, please send a cover letter together with your C.V. to: <span>info@corbelestates.com</span></p>
  <div class="btn btn-navy" style="left:887px;top:66px;width:112px">Send Your CV</div>
</section>

<!-- team -->
<section class="team-bg">
  <svg class="abs" style="left:0;top:0" width="1200" height="556" aria-hidden="true">
    <polygon points="1050,0 1050,490 720,490" fill="var(--sky)"/>
  </svg>
</section>
<div class="sec-title head" style="left:0;width:1200px;text-align:center;top:2318px"><b>Meet</b> The Team</div>
<div class="photo member" style="left:201px" role="img" aria-label="Portrait of a team member in a suit"><div class="who"><div class="n">DANIEL MORROW</div><div class="r">Outside Counsel - Hollis Barrett</div></div></div>
<div class="photo member" style="left:469px" role="img" aria-label="Portrait of a team member in a suit"><div class="who"><div class="n">DANIEL MORROW</div><div class="r">Outside Counsel - Hollis Barrett</div></div></div>
<div class="photo member" style="left:738px;background:linear-gradient(180deg,#a8875a 0%,#5a4a3c 45%,#1e2a38 100%)" role="img" aria-label="Portrait of a team member"><div class="who"><div class="n">LAURA WHITFIELD</div><div class="r">Outside RE Counsel - Ashford Lane</div></div></div>
<div class="btn btn-blue" style="left:563px;top:2723px;width:74px">View All</div>

<!-- partners & clients -->
<div class="col-title head" style="left:243px"><b>Corporate</b> Partners</div>
<div class="col-title head" style="left:656px"><b>Our</b> Clients</div>
<div class="divider"></div>
<div class="mark" style="left:312px;top:2910px;color:#1d2b3a"><i style="border:2px solid #f1b51c;border-radius:50%"></i>NORVIK</div>
<div class="mark" style="left:474px;top:2910px;color:#c8463c">HALDEN</div>
<div class="mark" style="left:393px;top:2960px;color:#2a49a8"><i style="background:#e2443a;border-radius:50%"></i>Quarra</div>
<div class="mark" style="left:320px;top:3011px;color:#2bb06a">BRISEL</div>
<div class="mark" style="left:469px;top:3011px;color:#f0b21f">OAKMERE</div>
<div class="mark" style="left:722px;top:2910px;color:#888"><i style="background:#999"></i>Tavio</div>
<div class="mark" style="left:886px;top:2910px;color:#888"><i style="border:2px solid #999"></i>Ferro</div>
<div class="mark" style="left:804px;top:2963px;color:#888">Corda</div>
<div class="mark" style="left:731px;top:3013px;color:#888"><i style="border:2px solid #999;border-radius:50%"></i>Vantis</div>
<div class="mark" style="left:878px;top:3013px;color:#888">Ostra</div>

<!-- footer -->
<footer class="footer">
  <div class="faint" style="left:1050px;top:190px;width:110px;height:110px;border-color:rgba(255,255,255,.07)"></div>
  <div class="brand" style="left:200px;top:81px"><span class="brand-dot"></span><span><span style="color:var(--blue)">Corbel</span> Estates</span></div>
  <div class="f-head" style="left:487px;top:60px">CONTACT INFO</div>
  <div class="f-line" style="top:94px;font-family:'Teko',sans-serif;font-size:17px;line-height:17px;align-items:center">
    <svg width="10" height="12" viewBox="0 0 10 12"><path d="M2 1l2 2-1 2 3 3 2-1 2 2-1.5 2C4 11 0 6 1 2z" fill="#1f9ad8"/></svg>(214) 555-0192</div>
  <div class="f-line" style="top:122px"><svg width="10" height="10" viewBox="0 0 10 10"><rect x=".5" y="1.5" width="9" height="7" fill="none" stroke="#1f9ad8"/><path d="M.5 1.5 5 5.5 9.5 1.5" fill="none" stroke="#1f9ad8"/></svg>info@corbelestates.com</div>
  <div class="f-line" style="top:143px"><svg width="10" height="12" viewBox="0 0 10 12"><path d="M5 12S1 7 1 4.5a4 4 0 0 1 8 0C9 7 5 12 5 12z" fill="#1f9ad8"/><circle cx="5" cy="4.5" r="1.4" fill="#0f3360"/></svg>4800 Linden Ave, 7th Floor<br>Dallas, Texas 75204</div>
  <div class="f-head" style="left:487px;top:204px">FOLLOW US</div>
  <div class="f-head" style="left:718px;top:60px">SEND US MESSAGE</div>
  <div class="field" style="left:718px;top:91px;width:133px;height:24px">Name</div>
  <div class="field" style="left:866px;top:91px;width:133px;height:24px">Phone</div>
  <div class="field" style="left:718px;top:128px;width:281px;height:24px">Email</div>
  <div class="field" style="left:718px;top:155px;width:281px;height:53px">Message</div>
  <div class="btn btn-blue" style="left:718px;top:223px;width:87px">Send</div>
  <div class="abs" style="left:200px;top:231px;font-size:8.5px;white-space:nowrap">© 2022 <span style="color:var(--blue)">Corbel Estates</span>. All Rights Reserved.</div>
</footer>
<div class="social" role="img" aria-label="Social profile" style="left:491px"></div>
<div class="social" role="img" aria-label="Social profile" style="left:528px"></div>

</body>
</html>
```